Business Card Design

I have a very clear idea of what I want. I just do not know how to do the graphic design to match it.

On the front I want the uploaded image with the horse and the two people.
I want

Bottom left hand corner
Lewis Brand
0438 512 607

Bottom right
There is maroon block with Neil Patton Practitioner Group Logo
Next to that I want the Stable Arc tile about the same size ( attached psd file)

On the back I want a plain colour (white) with the information

Lewis Brand
Equine Performance
Rowland4Ponies and Acupuncture
Horsemanship Lessons and Clinics
Horse Training

lbrand@fauna812.com.au
FB/lewis.brand.207
StableArc.com.au

Industry/Entity Type

Business

Contact Information for Business Card

Lewis Brand
0438 512 607
lbrand@fauna812.com.au

```html
<!DOCTYPE html>
<html lang="en">
<head>
<meta charset="utf-8">
<title>Lewis Brand – Business Card</title>
<link rel="stylesheet" href="https://fonts.googleapis.com/css2?family=Open+Sans:ital,wght@0,400;0,600;0,700;1,400&family=Dancing+Script:wght@700&display=swap">
<style>
  :root {
    --page-bg: #ece8e2;
    --sand-light: #e3cfa2;
    --sand-mid: #caa670;
    --sand-dark: #9c7a4a;
    --ink-brown: #4a2e1c;
    --maroon: #6e2c1f;
    --navy: #1d4f8c;
    --grey-text: #6b6b6b;
    --rule: #cfcfcf;
    --tile-rim: #7a4a2c;
    --white: #ffffff;
  }
  * { box-sizing: border-box; margin: 0; padding: 0; }
  html, body { width: 1200px; height: 950px; overflow: hidden; }
  body {
    background: var(--page-bg);
    font-family: "Open Sans", Arial, sans-serif;
    position: relative;
  }
  .card {
    position: absolute;
    width: 640px;
    height: 366px;
    border-radius: 4px;
    overflow: hidden;
    box-shadow: 0 6px 18px rgba(0,0,0,.18);
  }

  /* Front */
  .card-front { left: 70px; top: 80px; }
  .front-photo {
    position: absolute; inset: 0;
    background: radial-gradient(ellipse at 60% 45%, var(--sand-light) 0%, var(--sand-mid) 65%, var(--sand-dark) 100%);
  }
  .tagline {
    position: absolute; left: 34px; top: 70px;
    color: var(--ink-brown);
  }
  .tagline-lead {
    font-size: 15px; font-weight: 600; letter-spacing: 3px;
    text-transform: uppercase;
  }
  .tagline-main {
    font-family: "Dancing Script", cursive;
    font-size: 84px; line-height: 1; margin-top: 4px;
  }
  .front-contact {
    position: absolute; left: 34px; bottom: 30px;
    color: var(--ink-brown);
  }
  .front-name { font-size: 30px; font-weight: 700; line-height: 1.1; }
  .front-phone { font-size: 30px; font-weight: 700; line-height: 1.1; }
  .partner-block {
    position: absolute; right: 34px; bottom: 30px;
    display: flex; gap: 14px; align-items: flex-end;
  }
  .partner-maroon {
    width: 110px; height: 84px;
    background: var(--maroon);
    color: var(--sand-light);
    font-size: 11px; font-weight: 600; line-height: 1.3;
    display: flex; align-items: center; justify-content: center; text-align: center;
    padding: 8px;
  }
  .brand-tile {
    width: 84px; height: 84px; border-radius: 12px;
    background: var(--white);
    border: 4px solid var(--tile-rim);
    display: flex; align-items: center; justify-content: center;
    color: var(--navy); font-size: 14px; font-weight: 700;
  }

  /* Back */
  .card-back { left: 490px; top: 500px; background: var(--white); }
  .back-tile {
    position: absolute; left: 40px; top: 36px;
    width: 130px; height: 130px; border-radius: 18px;
    background: var(--white);
    border: 6px solid var(--tile-rim);
    box-shadow: 6px 6px 0 var(--tile-rim);
    display: flex; align-items: center; justify-content: center;
    color: var(--navy); font-size: 22px; font-weight: 700;
  }
  .back-rule {
    position: absolute; left: 40px; right: 40px; top: 196px;
    height: 1px; background: var(--rule);
  }
  .back-info {
    position: absolute; right: 40px; top: 36px; text-align: right;
  }
  .back-name { color: var(--navy); font-size: 24px; font-weight: 700; margin-bottom: 6px; }
  .back-role { color: var(--grey-text); font-style: italic; font-size: 15px; line-height: 1.45; }
  .back-contacts {
    position: absolute; left: 40px; top: 218px;
    list-style: none;
  }
  .back-contacts li {
    display: flex; align-items: center; gap: 10px;
    color: var(--grey-text); font-style: italic; font-size: 15px; line-height: 1.9;
  }
  .icon { width: 16px; height: 16px; flex: none; }
  .icon-square { width: 14px; height: 14px; background: var(--navy); border-radius: 2px; flex: none; margin: 0 1px; }
</style>
</head>
<body>

<section class="card card-front">
  <div class="front-photo" role="img" aria-label="Overhead photo of a trainer leading a dark horse across a sandy arena while a second person walks in front"></div>
  <div class="tagline">
    <p class="tagline-lead">How you ever gonna know</p>
    <p class="tagline-main">Your Potential</p>
  </div>
  <div class="front-contact">
    <p class="front-name">Lewis Brand</p>
    <p class="front-phone">0438 512 607</p>
  </div>
  <div class="partner-block">
    <div class="partner-maroon">Neil Patton Practitioner Group</div>
    <div class="brand-tile">Stable Arc</div>
  </div>
</section>

<section class="card card-back">
  <div class="back-tile">Stable Arc</div>
  <div class="back-info">
    <p class="back-name">Lewis Brand</p>
    <p class="back-role">Equine Performance</p>
    <p class="back-role">Rowland4Ponies &amp; Acupuncture</p>
    <p class="back-role">Horsemanship Lessons &amp; Clinics</p>
    <p class="back-role">Horse Training</p>
  </div>
  <div class="back-rule"></div>
  <ul class="back-contacts">
    <li>
      <svg class="icon" viewBox="0 0 16 16"><rect x="1" y="3" width="14" height="10" rx="1" fill="var(--navy)"/><path d="M1.5 4 L8 9 L14.5 4" fill="none" stroke="#fff" stroke-width="1.3"/></svg>
      lbrand@fauna812.com.au
    </li>
    <li>
      <svg class="icon" viewBox="0 0 16 16"><circle cx="8" cy="8" r="7" fill="var(--navy)"/><ellipse cx="8" cy="8" rx="3" ry="7" fill="none" stroke="#fff" stroke-width="1"/><line x1="1" y1="8" x2="15" y2="8" stroke="#fff" stroke-width="1"/></svg>
      StableArc.com.au
    </li>
    <li>
      <span class="icon-square"></span>
      FB/lewis.brand.207
    </li>
  </ul>
</section>

</body>
</html>
```